依頼詳細
★TOPラフ案について

・トップページの掲載内容はエクセルで作成した資料を添付しました。
仕様はワイヤーフレームのみですので、掲載情報が正しければ、お好きなデザインにて調整していただいて構いません。

掲載している情報のレイアウト通りではなくて大丈夫ですので
皆さまの感性にてお願いいたします。

・配置やデザイン等はアレンジしていただいて構いません。

・サイズは横幅2000pxで制作をお願いします。
縦に制限はありません。(コンテンツ幅は1100px~1200px内でお願いします。)
レスポンシブデザインのサイトで、bootstrap4を利用し、コーディングする予定になります。

・カラーイメージ
白を基調としてサブに青系、ワンポイントに赤色にてお願いします。

・ロゴ画像はヘッダーに入れる予定です。
(ロゴは青色(#00008B)で会社名ローマ字表示となります。頭文字は赤色(#FF3737)です。)

・デザインイメージ
誠実なデザインのイメージです。

デザイン選定後、決定した方には、正式な社名や連絡先を入れた修正をお願いしたいのと、
その他常識範囲で修正を依頼することもあります。
※以後、希望があれば中ページ作成及び他の案件コンテンツも継続してご依頼可能です。
ページ数
1ページ
希望イメージ
シンプル 複雑
単色 カラフル
暗い 明るい
日常 高級
遊び心 厳粛
未来的 伝統的
女性的 男性的
希望する色
青系
納品ファイル
• 高解像度JPG (.jpg)
• フォトショップ形式 (.psd)
補足説明
※ワイヤーフレーム通りのデザインでなくて、構いません。
メインビジュアル、素材などもお好みでデザインいただいて問題ございません。

仕様素材につきましてはZELNO定額素材内で使用可能な素材をご選択いただいてご使用ください。
(添付したデータ内にない素材でもご利用OKです。
その際は選定後素材№をお知らせください。)
■ 選んだ理由

依頼したイメージに沿ったデザインを作成いただけたためこちらのデザインに決めさせていただきました。

■ 提案者全員のお礼・コメント

多くの提案をいただき本当にありがとうございました。
次回の依頼の際も是非提案いただけますようお願いいたします。

```html
<!DOCTYPE html>
<html lang="ja">
<head>
<meta charset="utf-8">
<title>梱包が変わると物流が変わる</title>
<link href="https://fonts.googleapis.com/css2?family=Noto+Sans+JP:wght@400;500;700&family=Noto+Serif+JP:wght@500;700&family=Roboto:wght@500;700&display=swap" rel="stylesheet">
<style>
:root{
  --blue:#1f6fc9;
  --blue-deep:#00008b;
  --red:#ff3737;
  --ink:#333;
  --muted:#666;
  --line:#dcdcdc;
  --page:#f7f7f7;
  --dark:#2f2f2f;
  --foot:#e6e6e6;
}
*{margin:0;padding:0;box-sizing:border-box}
html,body{width:1200px;height:3144px;overflow:hidden}
body{background:var(--page);font-family:"Noto Sans JP",sans-serif;color:var(--ink);position:relative}
.abs{position:absolute}

/* header */
.site-header{position:absolute;left:0;top:0;width:1200px;height:80px;background:#fff;display:flex;align-items:center}
.brand{margin-left:32px;font-family:"Roboto",sans-serif;font-weight:700;font-size:24px;color:var(--blue-deep);letter-spacing:1px;display:flex;align-items:center;gap:8px}
.brand i{width:10px;height:10px;background:var(--red);display:block}
.global-nav{display:flex;gap:28px;margin-left:auto;font-size:11px;color:var(--muted)}
.header-tel{margin-left:36px;display:flex;align-items:center;gap:8px;font-family:"Roboto",sans-serif;font-weight:700;font-size:21px;color:var(--blue)}
.header-tel small{font-family:"Noto Sans JP",sans-serif;font-size:10px;font-weight:500;color:var(--blue);line-height:1.2}
.header-mail{margin-left:24px;width:180px;height:80px;background:var(--blue);color:#fff;font-size:13px;display:flex;align-items:center;justify-content:center;gap:8px}

/* hero */
.hero{position:absolute;left:0;top:80px;width:1200px;height:560px;background:linear-gradient(180deg,#9aa3ab 0%,#c7c3ba 45%,#8c8f92 100%)}
.hero-copy{position:absolute;left:0;top:285px;width:1200px;text-align:center;font-family:"Noto Serif JP",serif;font-weight:700;color:#fff;font-size:56px;letter-spacing:4px;text-shadow:0 2px 8px rgba(0,0,0,.35)}
.hero-copy span{font-size:38px}

/* section headings */
.mark{position:absolute;width:36px;height:36px}
.mark::before{content:"";position:absolute;left:0;top:0;width:24px;height:24px;background:var(--red)}
.mark::after{content:"";position:absolute;left:12px;top:12px;width:24px;height:24px;background:var(--dark)}
.heading{position:absolute;font-family:"Roboto",sans-serif;font-weight:700;font-size:40px;color:var(--blue);letter-spacing:1px;line-height:1}
.sub{position:absolute;font-size:13px;color:var(--muted)}
.center{width:1200px;left:0;text-align:center}

/* information */
.news{position:absolute;left:100px;top:860px;width:1000px;height:340px;background:#fff;border:1px solid var(--line)}
.news ul{list-style:none;padding:60px 0 0 120px;width:920px}
.news li{display:flex;align-items:center;height:48px;border-bottom:1px solid var(--line);font-size:12px}
.news time{width:60px}
.news .new{background:var(--red);color:#fff;font-size:9px;padding:1px 5px;margin-right:12px}
.news .gap{width:46px}
.scroll{position:absolute;right:8px;top:10px;width:14px;height:318px;background:#eee}
.scroll i{position:absolute;left:2px;top:205px;width:10px;height:70px;background:#bbb}

/* media blocks */
.photo{position:absolute}
.body-text{position:absolute;font-size:13px;line-height:2;color:var(--ink)}
.btn-more{position:absolute;width:120px;height:36px;background:var(--dark);color:#fff;font-size:11px;display:flex;align-items:center;justify-content:center}

/* contact band */
.contact-tel{position:absolute;left:0;top:2640px;width:600px;height:220px;background:var(--dark);color:#fff}
.contact-mail{position:absolute;left:600px;top:2640px;width:600px;height:220px;background:var(--blue);color:#fff}

/* footer */
.foot-nav{position:absolute;left:0;top:2862px;width:1200px;text-align:center;font-size:11px;color:var(--muted)}
.site-footer{position:absolute;left:0;top:2900px;width:1200px;height:220px;background:var(--foot)}
.btn-map,.btn-link{position:absolute;top:3020px;height:50px;color:#fff;font-size:14px;font-weight:500;display:flex;align-items:center;justify-content:center}
.btn-map{left:620px;width:200px;background:var(--dark)}
.btn-link{left:860px;width:260px;background:var(--red)}
.copyright{position:absolute;left:0;top:3126px;width:1200px;text-align:center;font-size:9px;color:#888}
</style>
</head>
<body>

<header class="site-header">
  <div class="brand"><i></i>ZELNO</div>
  <nav class="global-nav"><span>会社案内</span><span>業務案内</span><span>お知らせ</span><span>お問い合わせ</span></nav>
  <div class="header-tel">
    <svg width="20" height="20" viewBox="0 0 24 24"><path fill="#1f6fc9" d="M6.6 10.8a15 15 0 006.6 6.6l2.2-2.2a1 1 0 011-.25 11.4 11.4 0 003.6.57 1 1 0 011 1V20a1 1 0 01-1 1A17 17 0 013 4a1 1 0 011-1h3.5a1 1 0 011 1 11.4 11.4 0 00.57 3.6 1 1 0 01-.25 1z"/></svg>
    0120-00-1234<small>受付時間<br>9:00-17:00</small>
  </div>
  <a class="header-mail">
    <svg width="18" height="14" viewBox="0 0 18 14"><rect x="0.5" y="0.5" width="17" height="13" fill="none" stroke="#fff"/><path d="M1 1l8 6 8-6" fill="none" stroke="#fff"/></svg>
    メールお問い合わせ
  </a>
</header>

<section class="hero" role="img" aria-label="段ボール箱が並ぶ倉庫の棚の写真">
  <h1 class="hero-copy">梱包<span>が</span>変わる<span>と</span>物流<span>が</span>変わる</h1>
</section>

<section>
  <div class="mark" style="left:572px;top:700px"></div>
  <h2 class="heading center" style="top:748px">INFORMATION</h2>
  <p class="sub center" style="top:794px">お知らせ</p>
  <div class="news">
    <ul>
      <li><time>2021/7/3</time><span class="new">NEW</span>お知らせに関するテキストが入ります。お知らせに関するテキストが入ります。</li>
      <li><time>2021/7/3</time><span class="gap"></span>お知らせに関するテキストが入ります。お知らせに関するテキストが入ります。</li>
      <li><time>2021/7/3</time><span class="gap"></span>お知らせに関するテキストが入ります。お知らせに関するテキストが入ります。</li>
      <li><time>2021/7/3</time><span class="gap"></span>お知らせに関するテキストが入ります。お知らせに関するテキストが入ります。</li>
      <li><time>2021/7/3</time><span class="gap"></span>お知らせに関するテキストが入ります。お知らせに関するテキストが入ります。</li>
    </ul>
    <div class="scroll"><i></i></div>
  </div>
</section>

<section>
  <div class="mark" style="left:240px;top:1372px"></div>
  <h2 class="heading" style="left:300px;top:1408px">ABOUT</h2>
  <p class="sub" style="left:300px;top:1450px">会社案内</p>
  <p class="body-text" style="left:140px;top:1520px;width:440px">20XX年に○○○○より分社独立し創業した「株式会社○○○○」<br>梱包のスペシャリスト集団が最適なサービスをお約束します。</p>
  <a class="btn-more" style="left:300px;top:1630px">詳しく見る</a>
  <div class="photo" role="img" aria-label="倉庫の搬入口に並ぶトラックの荷台の写真" style="left:640px;top:1380px;width:440px;height:440px;background:linear-gradient(135deg,#d9dde2,#a9b0b8)"></div>
</section>

<section>
  <div class="photo" role="img" aria-label="段ボール箱を抱える作業員の手元の写真" style="left:100px;top:1940px;width:460px;height:420px;background:linear-gradient(135deg,#c4b49a,#8e8a86)"></div>
  <div class="mark" style="left:740px;top:1950px"></div>
  <h2 class="heading" style="left:800px;top:1980px">PACKING</h2>
  <p class="sub" style="left:800px;top:2022px">業務案内</p>
  <p class="body-text" style="left:740px;top:2090px;width:360px">梱包の専門企業として、お客様のニーズに合った<br>資材・梱包・ラベル作業などを提供しています。<br>キーワードでお客様に最適な方法をご提案。<br>「梱包の最適化」</p>
  <a class="btn-more" style="left:740px;top:2260px">詳しく見る</a>
</section>

<section>
  <div class="mark" style="left:572px;top:2484px"></div>
  <h2 class="heading center" style="top:2534px">CONTACT US</h2>
  <p class="sub center" style="top:2580px">お問い合わせ</p>
  <div class="contact-tel">
    <p class="abs" style="left:0;top:40px;width:600px;text-align:center;font-size:13px">お電話でのお問い合わせ</p>
    <p class="abs" style="left:150px;top:92px;font-family:'Roboto',sans-serif;font-weight:700;font-size:40px;letter-spacing:1px">TEL. 0120-00-1234</p>
    <p class="abs" style="left:330px;top:152px;font-size:11px">9:00〜17:00（平日）</p>
  </div>
  <div class="contact-mail">
    <p class="abs" style="left:0;top:40px;width:600px;text-align:center;font-size:13px">メールでのお問い合わせ</p>
    <div class="abs" style="left:120px;top:96px;display:flex;align-items:center;gap:14px;font-size:28px;font-weight:700">
      <svg width="36" height="26" viewBox="0 0 36 26"><rect x="1" y="1" width="34" height="24" fill="none" stroke="#fff" stroke-width="2"/><path d="M2 2l16 12L34 2" fill="none" stroke="#fff" stroke-width="2"/></svg>
      メールフォームはこちら
    </div>
  </div>
</section>

<p class="foot-nav">ホーム ｜ 会社案内 ｜ 業務案内 ｜ お知らせ ｜ お問い合わせ</p>
<footer class="site-footer">
  <p class="abs" style="left:80px;top:60px;font-size:22px;font-weight:500">株式会社○○○○</p>
  <p class="abs" style="left:80px;top:104px;font-size:16px">〒111-1111 東京都○○区○○町1丁目1-1</p>
  <p class="abs" style="left:80px;top:140px;font-size:11px;line-height:1.8">TEL：00-0000-0000<br>FAX：00-0000-0000</p>
</footer>
<a class="btn-map">MAP</a>
<a class="btn-link">リンク</a>
<p class="copyright">© 株式会社○○○○ All Rights Reserved.</p>

</body>
</html>
```